Lorna Vee Tresses Fancy Business Card’s

I want my business cards to be elite, original and very classy. I want the business cards to match the colors of my logo and to match the design posted. I would love the design of the picture I posted

I want the card all white .
The dripping on the top of the card I want it to match the pink color in my logo that’s also posted .
I need my logo on the business card !
I need my Instagram- @lorna.vee.tresses__
And my phone number - 555 207 9362

Target Market(s)

My target market is young woman age 23 to older woman to the age of 65
I want both older and younger women to love my design . I don’t want any cheap looking business cards

Industry/Entity Type

Hair And Beauty

Contact Information for Business Card

Add my logo
Add my Instagram- @lorna.vee.tresses__
My number - 555 207 9362
My website- www.lornaveetresses-example.com

Font styles to use
Serif
Script

Colors
ffffff
e667a6
e34298

Requirements
Must have
• The business cards must have my logo, my number , my website, and my Instagram!
Nice to have
• Nice to have glitter words that match my logo
• The business cards must look classy and mature
• I want them to be very unique!!
Should not have
• Should not have any colors that doesn’t match my logo ! This is very important! Please

```html
<!DOCTYPE html>
<html lang="en">
<head>
<meta charset="utf-8">
<title>Lorna Vee Tresses – Business Card</title>
<link rel="stylesheet" href="https://fonts.googleapis.com/css2?family=Great+Vibes&family=Montserrat:wght@400&family=Open+Sans:wght@400&family=Playfair+Display:wght@700&display=swap">
<style>
  :root {
    --backdrop: #2f2f2f;
    --card: #1f1f1f;
    --pink: #e34298;
    --pink-soft: #e667a6;
    --silver: #cfcfcf;
    --white: #ffffff;
  }
  * { box-sizing: border-box; margin: 0; padding: 0; }
  html, body {
    width: 1200px;
    height: 901px;
    overflow: hidden;
    background: var(--backdrop);
  }
  .stage {
    position: relative;
    width: 1200px;
    height: 901px;
  }
  .card {
    position: absolute;
    left: 320px;
    width: 560px;
    height: 320px;
    background: var(--card);
    overflow: hidden;
  }
  .card::after {
    content: "";
    position: absolute;
    left: 0; right: 0; bottom: 0;
    height: 14px;
    background: var(--pink);
  }
  .card--front { top: 110px; }
  .card--back { top: 470px; }

  .brand {
    position: absolute;
    left: 0; right: 0; top: 0; bottom: 14px;
    display: flex;
    align-items: center;
    justify-content: center;
  }
  .brand__name {
    font-family: "Playfair Display", Georgia, serif;
    font-weight: 700;
    font-size: 44px;
    color: var(--silver);
    letter-spacing: 1px;
  }

  .person {
    position: absolute;
    right: 340px;
    top: 116px;
    text-align: right;
  }
  .person__name {
    font-family: "Great Vibes", cursive;
    font-size: 40px;
    line-height: 1;
    color: var(--pink);
    white-space: nowrap;
  }
  .person__role {
    font-family: "Montserrat", Arial, sans-serif;
    font-size: 15px;
    color: var(--white);
    margin-top: 6px;
  }
  .divider {
    position: absolute;
    left: 238px;
    top: 112px;
    width: 1.5px;
    height: 88px;
    background: var(--white);
  }
  .contacts {
    position: absolute;
    left: 256px;
    top: 122px;
    list-style: none;
    font-family: "Open Sans", Arial, sans-serif;
    font-size: 14px;
    color: var(--white);
  }
  .contacts__item {
    display: flex;
    align-items: center;
    gap: 8px;
    height: 23px;
    white-space: nowrap;
  }
  .contacts__icon { width: 14px; height: 14px; flex: none; }
  .contacts__dot {
    width: 11px; height: 11px; flex: none;
    margin: 0 1.5px;
    background: var(--pink-soft);
  }
  .contacts__dot--round { border-radius: 50%; }
</style>
</head>
<body>
<main class="stage">
  <section class="card card--front" aria-label="Card front">
    <div class="brand">
      <span class="brand__name">Lorna Vee Tresses</span>
    </div>
  </section>

  <section class="card card--back" aria-label="Card back">
    <div class="person">
      <p class="person__name">Delia Marsh</p>
      <p class="person__role">Manager</p>
    </div>
    <div class="divider"></div>
    <ul class="contacts">
      <li class="contacts__item">
        <svg class="contacts__icon" viewBox="0 0 24 24" aria-hidden="true">
          <path fill="#e667a6" d="M6.6 10.8a15.1 15.1 0 0 0 6.6 6.6l2.2-2.2a1 1 0 0 1 1-.25 11.4 11.4 0 0 0 3.6.57 1 1 0 0 1 1 1V20a1 1 0 0 1-1 1A17 17 0 0 1 3 4a1 1 0 0 1 1-1h3.5a1 1 0 0 1 1 1c0 1.250.2 2.450.57 3.6a1 1 0 0 1-.25 1z"/>
        </svg>
        <span>555 207 9362</span>
      </li>
      <li class="contacts__item">
        <span class="contacts__dot" aria-hidden="true"></span>
        <span>@lorna.vee.tresses__</span>
      </li>
      <li class="contacts__item">
        <span class="contacts__dot contacts__dot--round" aria-hidden="true"></span>
        <span>www.lornaveetresses-example.com</span>
      </li>
    </ul>
  </section>
</main>
</body>
</html>
```